Cybersecurity company is looking for business card.

I need a business card design for our company, we are a cybersecurity company providing advance technology to protect agains any kind of malware. We need a fresh modern design it should communicate modern, technology and growth.

Target Market(s)

Business to business

Industry/Entity Type

Business

Contact Information for Business Card

Should have location, address, fax, mobile, phone, email and website.

Requirements
Must have
• Must follow company's logo color and style. Must have the company's log on its.

```html
<!DOCTYPE html>
<html lang="en">
<head>
<meta charset="utf-8">
<title>Veltrox Business Card</title>
<link rel="stylesheet" href="https://fonts.googleapis.com/css2?family=Arimo:wght@400;600;700&display=swap">
<style>
  :root {
    --ink: #07080a;
    --brand-red: #a01f22;
    --paper: #ffffff;
    --text: #1a1a1a;
    --edge: #7a7a7a;
  }
  * { margin: 0; padding: 0; box-sizing: border-box; }
  html, body { width: 1200px; height: 1000px; overflow: hidden; background: var(--paper); }
  body { position: relative; font-family: "Arimo", Arial, sans-serif; color: var(--text); }

  .card { position: absolute; width: 566px; height: 354px; overflow: hidden; }

  /* Front */
  .card-front { left: 31px; top: 136px; height: 353px; background: var(--ink); }
  .front-band {
    position: absolute; left: 98px; top: 116px; width: 468px; height: 121px;
    background: var(--brand-red); border-radius: 61px 0 0 61px;
  }
  .front-brand { position: absolute; right: 159px; top: 142px; text-align: right; color: var(--paper); }
  .front-brand .brand-name { font-size: 56px; font-weight: 700; line-height: 1; letter-spacing: 1px; }
  .front-brand .brand-tagline { font-size: 15px; font-weight: 400; margin-top: 2px; }

  /* Back */
  .card-back { left: 597px; top: 489px; background: var(--paper); border: 1px solid var(--edge); }
  .back-lines { position: absolute; left: 0; top: 0; }
  .contact-panel { position: absolute; left: 0; top: 147px; width: 99px; height: 207px; background: var(--brand-red); }

  .holder { position: absolute; right: 115px; top: 64px; text-align: right; }
  .holder-name { font-size: 21px; font-weight: 700; line-height: 1.1; }
  .holder-title { font-size: 14px; font-weight: 600; margin-top: 5px; }

  .contact-list { position: absolute; left: 0; top: 0; list-style: none; }
  .contact-item { position: absolute; left: 0; width: 360px; height: 24px; }
  .contact-icon { position: absolute; left: 64px; top: 0; width: 22px; height: 22px; }
  .contact-text { position: absolute; left: 110px; top: 3px; font-size: 14px; line-height: 18px; white-space: nowrap; }

  .back-brand { position: absolute; right: 47px; top: 278px; text-align: right; color: var(--ink); }
  .back-brand .brand-name { font-size: 35px; font-weight: 700; line-height: 1; letter-spacing: 0.5px; }
  .back-brand .brand-tagline { font-size: 10px; margin-top: 2px; }
</style>
</head>
<body>

<section class="card card-front" aria-label="Card front">
  <div class="front-band"></div>
  <div class="front-brand">
    <div class="brand-name">veltrox</div>
    <div class="brand-tagline">Cybersecurity Company</div>
  </div>
</section>

<section class="card card-back" aria-label="Card back">
  <svg class="back-lines" width="566" height="354" viewBox="0 0 566 354" aria-hidden="true">
    <path d="M517 0 V60 Q517 77 500 77 H475" fill="none" stroke="var(--ink)" stroke-width="2"/>
    <path d="M303 103 H66 Q50 103 50 119 V147" fill="none" stroke="var(--brand-red)" stroke-width="2"/>
  </svg>

  <div class="contact-panel"></div>

  <div class="holder">
    <div class="holder-name">Omar Haddad</div>
    <div class="holder-title">Managing Director</div>
  </div>

  <ul class="contact-list">
    <li class="contact-item" style="top:160px">
      <svg class="contact-icon" viewBox="0 0 22 22" aria-hidden="true"><path d="M2 11 L11 3 L20 11 H17 V19 H13 V14 H9 V19 H5 V11 Z" fill="#fff"/></svg>
      <span class="contact-text">Harbor Tech Park (HTP)<br>Coastal Avenue, Port City - UAE</span>
    </li>
    <li class="contact-item" style="top:207px">
      <svg class="contact-icon" viewBox="0 0 22 22" aria-hidden="true"><rect x="6" y="1.5" width="10" height="19" rx="2" fill="none" stroke="#fff" stroke-width="1.6"/><circle cx="11" cy="17" r="1" fill="#fff"/></svg>
      <span class="contact-text">+000 52 123 XXXX</span>
    </li>
    <li class="contact-item" style="top:242px">
      <svg class="contact-icon" viewBox="0 0 22 22" aria-hidden="true"><path d="M5 2 L8 2 L10 7 L7.5 9 Q9.5 13.5 13 15 L15 12.5 L20 14.5 V17.5 Q19.5 20 17 20 Q3 19 2 5 Q2 2.5 5 2 Z" fill="none" stroke="#fff" stroke-width="1.4" stroke-linejoin="round"/></svg>
      <span class="contact-text">00 123 XXXX</span>
    </li>
    <li class="contact-item" style="top:276px">
      <svg class="contact-icon" viewBox="0 0 22 22" aria-hidden="true"><rect x="2" y="5" width="18" height="13" fill="#fff"/><path d="M2 5 L11 12 L20 5" fill="none" stroke="var(--brand-red)" stroke-width="1.4"/></svg>
      <span class="contact-text">name.surname@veltrox.com</span>
    </li>
    <li class="contact-item" style="top:306px">
      <svg class="contact-icon" viewBox="0 0 22 22" aria-hidden="true"><g fill="none" stroke="#fff" stroke-width="1.4"><circle cx="11" cy="11" r="9"/><ellipse cx="11" cy="11" rx="4" ry="9"/><path d="M2 11 H20 M4 6 H18 M4 16 H18"/></g></svg>
      <span class="contact-text">www.veltrox.com</span>
    </li>
  </ul>

  <div class="back-brand">
    <div class="brand-name">veltrox</div>
    <div class="brand-tagline">Cybersecurity Company</div>
  </div>
</section>

</body>
</html>
```